Pro-life non-profit needs a dynamic poster design for their Christmas Gala.

We need a poster design which plays off the name of the event, The Winter Lantern. The Winter Lantern, of course is the Baby Jesus. Our cause supports unborn children in Iowa. The gala will include a concert of popular Christmas music sung by top soloists backed by an orchestra. An original commissioned song, The Winter Lantern, will be premiered. Purple and gold colors immediately come to mind, but a designer should not feel constrained on colors. We need an editable design w/fonts. Photoshop w/layers or Illustrator files are good.

```html
<!DOCTYPE html>
<html lang="en">
<head>
<meta charset="utf-8">
<title>The Winter Lantern – A Pro Life Christmas Gala</title>
<link href="https://fonts.googleapis.com/css2?family=Bebas+Neue&family=Oswald:wght@300;400&family=Poppins:wght@500;700;800&family=Titan+One&display=swap" rel="stylesheet">
<style>
  :root {
    --crimson: #c62244;
    --crimson-deep: #a61d3b;
    --red: #e3101e;
    --gold-light: #fff6a8;
    --gold: #e8c536;
    --gold-deep: #8a6a12;
    --ink: #111111;
    --white: #ffffff;
    --blush: #f2c9d2;
  }
  * { margin: 0; padding: 0; box-sizing: border-box; }
  html, body { width: 1200px; height: 1200px; overflow: hidden; background: var(--white); }
  .canvas { position: relative; width: 1200px; height: 1200px; background: var(--white); }
  .poster {
    position: absolute; left: 277px; top: 169px;
    width: 1046px; height: 1354px;
    transform: scale(0.625); transform-origin: top left;
    overflow: hidden;
    background: linear-gradient(160deg, var(--crimson) 0%, var(--crimson-deep) 100%);
  }
  .poster p, .poster h1 { white-space: nowrap; }
  .abs { position: absolute; }
  .center { left: 0; width: 100%; text-align: center; }
  .presenter {
    top: 48px; font-family: "Poppins", sans-serif; font-weight: 500;
    font-size: 23px; line-height: 1.2; color: var(--white); letter-spacing: 0.2px;
  }
  .title {
    top: 92px; font-family: "Titan One", sans-serif; font-size: 76px; line-height: 1;
    transform: scaleY(1.35); transform-origin: top center;
    background: linear-gradient(180deg, var(--gold-light) 0%, var(--gold) 45%, #b99418 60%, var(--gold-light) 100%);
    -webkit-background-clip: text; background-clip: text; color: transparent;
    -webkit-text-stroke: 2px var(--gold-deep);
    filter: drop-shadow(3px 4px 0 #2a1a05);
  }
  .subtitle {
    font-family: "Poppins", sans-serif; font-weight: 800; color: var(--white); line-height: 1;
    -webkit-text-stroke: 1.5px var(--ink); paint-order: stroke fill;
    text-shadow: 2px 3px 0 var(--ink);
  }
  .subtitle-top { top: 200px; font-size: 36px; }
  .subtitle-main { top: 238px; font-size: 54px; }
  .panel { left: 0; top: 0; }
  .village { left: 160px; top: 305px; width: 710px; height: 105px; }
  .date-row {
    top: 462px; left: 249px; width: 548px; height: 58px;
    border-top: 2px solid var(--red); border-bottom: 2px solid var(--red);
    display: flex; font-family: "Bebas Neue", sans-serif; font-size: 48px; color: var(--ink); white-space: nowrap;
  }
  .date-row span { display: flex; align-items: center; justify-content: center; padding-top: 4px; }
  .date-day { width: 168px; border-right: 2px solid var(--red); }
  .date-month { width: 277px; border-right: 2px solid var(--red); }
  .date-year { flex: 1; }
  .accent { color: var(--red); }
  sup { font-size: 0.5em; vertical-align: 0.9em; line-height: 0; }
  .doors-wrap { top: 524px; }
  .doors {
    display: inline-block; font-family: "Bebas Neue", sans-serif; font-size: 46px; color: var(--ink);
    border-bottom: 2px solid var(--red); line-height: 52px; padding: 0 12px;
  }
  .venue { top: 586px; font-family: "Bebas Neue", sans-serif; font-size: 46px; color: var(--ink); }
  .venue-line { display: inline-block; border-bottom: 2px solid var(--ink); line-height: 48px; padding: 0 4px; }
  .feature-art { top: 690px; height: 110px; border-radius: 14px; }
  .feature-label { top: 806px; font-family: "Bebas Neue", sans-serif; font-size: 42px; line-height: 1.2; color: var(--ink); text-align: center; }
  .bullet { top: 821px; width: 10px; height: 10px; border-radius: 50%; background: var(--ink); }
  .speaker-frame {
    left: 357px; top: 926px; width: 362px; height: 46px;
    border: 2px solid var(--red); border-radius: 14px 14px 0 0; border-bottom: none;
    font-family: "Bebas Neue", sans-serif; font-size: 38px; text-align: center; line-height: 48px; color: var(--ink);
  }
  .speaker-name {
    left: 309px; top: 967px; width: 458px; height: 54px; background: var(--red);
    border-radius: 16px; font-family: "Bebas Neue", sans-serif; font-size: 50px;
    color: var(--white); text-align: center; line-height: 58px;
  }
  .megaphone { left: 240px; top: 927px; width: 90px; height: 92px; border-radius: 40% 20% 20% 40%; }
  .notice { top: 1074px; font-family: "Bebas Neue", sans-serif; font-size: 38px; line-height: 1.2; color: var(--ink); word-spacing: 2px; }
  .tickets { top: 1134px; font-family: "Oswald", sans-serif; font-weight: 300; font-size: 32px; color: var(--ink); display: flex; justify-content: center; align-items: center; gap: 12px; }
  .url { top: 1172px; font-family: "Oswald", sans-serif; font-weight: 400; font-size: 36px; line-height: 1.2; color: var(--red); }
  .contact { left: 172px; top: 1226px; font-family: "Oswald", sans-serif; font-weight: 400; font-size: 30px; line-height: 40px; color: var(--ink); }
  .dot { border-radius: 50%; background: radial-gradient(circle at 35% 35%, var(--gold-light), var(--gold) 60%, var(--gold-deep)); }
</style>
</head>
<body>
<div class="canvas">
  <main class="poster">
    <div class="abs dot" style="left:50px;top:232px;width:30px;height:30px"></div>
    <div class="abs dot" style="left:55px;top:655px;width:20px;height:20px"></div>
    <div class="abs dot" style="left:970px;top:1115px;width:12px;height:12px"></div>
    <div class="abs dot" style="left:105px;top:1238px;width:12px;height:12px"></div>

    <p class="abs center presenter">HEARTLAND HOPE ALLIANCE PRESENTS THE TENTH ANNUAL FUNDRAISING BANQUET</p>
    <h1 class="abs center title">THE WINTER LANTERN</h1>
    <p class="abs center subtitle subtitle-top">A PRO LIFE OF</p>
    <p class="abs center subtitle subtitle-main">CHRISTMAS GALA</p>

    <svg class="abs panel" width="1046" height="1354" viewBox="0 0 1046 1354">
      <path fill="#ffffff" d="M95 1354 V1040 Q95 1024 150 1024 Q95 1020 95 960 V600 Q95 420 250 395 H800 Q952 420 952 600 V1354 Z"/>
    </svg>
    <svg class="abs village" role="img" aria-label="White snowy village silhouette with houses and pine trees" viewBox="0 0 710 105" preserveAspectRatio="none">
      <defs><linearGradient id="snowTown" x1="0" y1="0" x2="0" y2="1"><stop offset="0" stop-color="#f6d9df"/><stop offset="0.5" stop-color="#ffffff"/></linearGradient></defs>
      <rect width="710" height="105" rx="20" fill="url(#snowTown)"/>
    </svg>

    <div class="abs date-row">
      <span class="date-day">SATURDAY</span>
      <span class="date-month">NOVEMBER&nbsp;<b class="accent" style="font-weight:400">21</b><sup>ST</sup></span>
      <span class="date-year">2020</span>
    </div>
    <div class="abs center doors-wrap">
      <p class="doors">DOORS OPEN AT <span class="accent">5:30</span><sup>PM</sup></p>
    </div>
    <p class="abs center venue"><span class="venue-line"><span class="accent">MAPLE HALL CENTER</span>, BROOKFIELD, IA</span></p>

    <div class="abs feature-art" role="img" aria-label="Illustration of three colourful cocktail glasses" style="left:160px;width:140px;background:linear-gradient(90deg,#f3b2c0,#f6a23c,#9ed36a)"></div>
    <div class="abs feature-art" role="img" aria-label="Illustration of guests around a round dinner table seen from above" style="left:412px;width:115px;border-radius:50%;background:radial-gradient(circle,#7a4a2a,#5a3620 70%,#3d4f7a)"></div>
    <div class="abs feature-art" role="img" aria-label="Illustration of a violinist and a drummer performing" style="left:665px;width:170px;background:linear-gradient(90deg,#2b2b33,#3b4f8a)"></div>
    <p class="abs feature-label" style="left:140px;width:190px">COCKTAILS</p>
    <span class="abs bullet" style="left:355px"></span>
    <p class="abs feature-label" style="left:400px;width:140px">DINNER</p>
    <span class="abs bullet" style="left:570px"></span>
    <p class="abs feature-label" style="left:620px;width:290px">CHRISTMAS CONCERT</p>

    <div class="abs megaphone" role="img" aria-label="Orange and white megaphone icon" style="background:linear-gradient(135deg,#f5f5f5,#f08a1c)"></div>
    <p class="abs speaker-frame">SPECIAL GUEST SPEAKER</p>
    <p class="abs speaker-name">BISHOP THOMAS ALBRIGHT</p>

    <p class="abs center notice">SEATING LIMITED &nbsp;|&nbsp; RESERVATIONS NEEDED</p>
    <div class="abs center tickets">
      <svg width="40" height="28" viewBox="0 0 40 28" aria-hidden="true"><rect x="3" y="5" width="34" height="18" rx="3" fill="none" stroke="#111" stroke-width="2"/><line x1="12" y1="5" x2="12" y2="23" stroke="#111" stroke-width="1.5" stroke-dasharray="2 2"/></svg>
      <span>Order tickets online</span>
    </div>
    <p class="abs center url">www.HeartlandHope.org</p>
    <div class="abs contact">
      <p>555-014-2290</p>
      <p>events@heartlandhope.org</p>
    </div>
  </main>
</div>
</body>
</html>
```